New Business Card

Would like a shiny card with Metallic logo raised on th front. Address 418 Kestwick Lane, Toronto Ontario M4T2B8, phone 416 555 0382, email kmvc@lorentel.ca and web www.kmvc.ca on the back in right and left lower corners balanced. Top of back should say Personalized Care for Pet's and their People centered. Leaving space on the back to write. Horizontal placement

```html
<!DOCTYPE html>
<html lang="en">
<head>
<meta charset="UTF-8">
<title>Kestwick Lane Animal Hospital — Business Card</title>
<link href="https://fonts.googleapis.com/css2?family=Michroma&family=Work+Sans:wght@400;500&display=swap" rel="stylesheet">
<style>
  :root {
    --backdrop: #111111;
    --card: #1d1d1d;
    --card-edge: #262626;
    --silver: #b9b9b9;
    --silver-bright: #d6d6d6;
    --ink-grey: #7d7d7d;
    --rule: #6a6a6a;
  }
  * { margin: 0; padding: 0; box-sizing: border-box; }
  html, body {
    width: 1200px; height: 900px; overflow: hidden;
    background: var(--backdrop);
  }
  .canvas {
    width: 1200px; height: 900px;
    display: flex; flex-direction: column; align-items: center; justify-content: center;
    gap: 44px;
  }
  .card {
    width: 640px; height: 366px;
    background: var(--card);
    border: 1px solid var(--card-edge);
    position: relative;
  }

  /* Front */
  .card--front {
    display: flex; flex-direction: column; align-items: center; justify-content: center;
  }
  .brand {
    display: flex; flex-direction: column; align-items: center;
    font-family: "Michroma", sans-serif;
    color: var(--silver-bright);
    text-align: center;
  }
  .brand__mark {
    width: 58px; height: 58px; border-radius: 50%;
    background: var(--silver-bright);
    margin-bottom: 16px;
  }
  .brand__name { font-size: 26px; letter-spacing: 1px; line-height: 1.1; }
  .brand__sub { font-size: 11px; letter-spacing: 2px; margin-top: 6px; }
  .tagline {
    margin-top: 34px;
    font-family: "Michroma", sans-serif;
    font-size: 12.5px; letter-spacing: 1.5px; line-height: 1.5;
    color: var(--silver);
    text-align: center;
    text-transform: uppercase;
  }

  /* Back */
  .card--back {
    display: flex; align-items: center;
    padding: 0 40px 0 34px;
  }
  .card--back .brand { color: var(--ink-grey); width: 300px; }
  .card--back .brand__mark { background: var(--ink-grey); width: 50px; height: 50px; }
  .card--back .brand__name { font-size: 22px; }
  .card--back .brand__sub { font-size: 10px; }
  .divider {
    width: 1px; height: 190px; background: var(--rule);
    margin: 0 28px 0 26px;
  }
  .contact {
    font-family: "Work Sans", sans-serif;
    color: var(--ink-grey);
  }
  .contact__name {
    font-weight: 500; font-size: 21px; letter-spacing: 2px; text-transform: uppercase;
  }
  .contact__role { font-size: 17px; margin-top: 2px; letter-spacing: 0.5px; }
  .contact__address { font-size: 15.5px; line-height: 1.3; margin-top: 20px; letter-spacing: 0.5px; }
  .contact__list { list-style: none; margin-top: 14px; font-size: 15.5px; letter-spacing: 0.5px; }
  .contact__list li { display: flex; align-items: center; gap: 10px; line-height: 1.6; }
  .icon { width: 13px; height: 13px; fill: var(--ink-grey); flex: none; }
  .icon--line { fill: none; stroke: var(--ink-grey); stroke-width: 1.4; }
</style>
</head>
<body>
<main class="canvas">
  <section class="card card--front" aria-label="Card front">
    <div class="brand">
      <span class="brand__mark"></span>
      <span class="brand__name">KESTWICK LANE</span>
      <span class="brand__sub">ANIMAL HOSPITAL</span>
    </div>
    <p class="tagline">Personalized care for pet's<br>and their people centered</p>
  </section>

  <section class="card card--back" aria-label="Card back">
    <div class="brand">
      <span class="brand__mark"></span>
      <span class="brand__name">KESTWICK LANE</span>
      <span class="brand__sub">ANIMAL HOSPITAL</span>
    </div>
    <span class="divider"></span>
    <div class="contact">
      <p class="contact__name">Daniel Rourke</p>
      <p class="contact__role">Founder</p>
      <p class="contact__address">418 Kestwick Lane,<br>Toronto Ontario M4T2B8</p>
      <ul class="contact__list">
        <li>
          <svg class="icon" viewBox="0 0 16 16" aria-hidden="true"><path d="M3.6 1.2l2.3 2.6-1.3 1.8c.9 2 2.5 3.6 4.5 4.6l1.8-1.3 2.6 2.3-1.2 2.4C7.5 13.8 2.2 8.5 1.2 3.6z"/></svg>
          <span>416 555 0382</span>
        </li>
        <li>
          <svg class="icon" viewBox="0 0 16 16" aria-hidden="true"><path d="M1 3.5h14v9H1z M1.6 4l6.4 5 6.4-5" fill="none" stroke="#7d7d7d" stroke-width="1.3"/></svg>
          <span>kmvc@lorentel.ca</span>
        </li>
        <li>
          <svg class="icon icon--line" viewBox="0 0 16 16" aria-hidden="true"><circle cx="8" cy="8" r="6.5"/><ellipse cx="8" cy="8" rx="2.8" ry="6.5"/><path d="M1.5 8h13M2.5 4.8h11M2.5 11.2h11"/></svg>
          <span>www.kmvc.ca</span>
        </li>
      </ul>
    </div>
  </section>
</main>
</body>
</html>
```